website redesign - bronwickhomes.com.au

need to redesign our website. we are proud of our current website but market feedback suggests that we have to tone down our quirkiness and make it look more professional to target the million dollar market.
right now we appeal to the younger generation so we have to meet somewhere in the middle.
we want to still retain our same flavour and style but need to also look a bit more professional. we need to evolve our brand to a more grown up look.
examples of standard websites include tallow estates, gant dwellings, lodger ledger, fennimore upward, dowsett

```html
<!DOCTYPE html>
<html lang="en">
<head>
<meta charset="utf-8">
<title>Bronwick Homes</title>
<link rel="stylesheet" href="https://fonts.googleapis.com/css2?family=Montserrat:wght@400;600;700;800&family=Roboto:wght@300;400;500;700&display=swap">
<style>
:root{
  --orange:#f15a24;
  --orange-2:#f7892f;
  --ink:#1a1a1a;
  --text:#4a4a4a;
  --muted:#9a9a9a;
  --line:#e2e2e2;
  --grey-bg:#f3f3f3;
  --footer:#2f2f31;
  --white:#ffffff;
}
*{box-sizing:border-box;margin:0;padding:0}
html,body{width:1200px;height:3607px;overflow:hidden}
body{position:relative;background:var(--white);font-family:Roboto,Arial,sans-serif;color:var(--text)}
.abs{position:absolute}
.brand{font-family:Montserrat,Arial,sans-serif;font-weight:600;letter-spacing:1px;color:var(--orange)}
.site-header{position:absolute;left:0;top:0;width:1200px;height:80px;background:var(--white)}
.site-header .brand{left:49px;top:27px;font-size:24px}
.main-nav a{position:absolute;top:32px;font-size:13px;color:#444;text-decoration:none}
.main-nav a.active{color:var(--orange)}
.phone{position:absolute;left:916px;top:28px;font-family:Montserrat,sans-serif;font-weight:700;font-size:18px;color:#666;display:flex;align-items:center;gap:6px}
.phone span{color:var(--orange)}
.hero{position:absolute;left:0;top:80px;width:1200px;height:560px;background:linear-gradient(180deg,#e4e4e2 0%,#dcdcda 55%,#cfcfcc 100%)}
.hero-title{position:absolute;left:0;top:132px;width:1200px;text-align:center;font-family:Montserrat,sans-serif;font-weight:800;font-size:39px;line-height:41px;color:var(--white);letter-spacing:.5px}
.search-box{position:absolute;left:139px;top:561px;width:922px;height:159px;background:var(--white);box-shadow:0 4px 16px rgba(0,0,0,.08)}
.search-box h2{position:absolute;left:0;top:25px;width:100%;text-align:center;font-family:Montserrat,sans-serif;font-weight:600;font-size:22px;color:#555}
.field{position:absolute;top:77px;height:42px;background:#f4f4f4;font-size:11px;color:#555;padding:16px 15px 0}
.field.select::after{content:"";position:absolute;right:10px;top:21px;border:3px solid transparent;border-top-color:#555}
.btn{position:absolute;background:linear-gradient(90deg,var(--orange),var(--orange-2));color:var(--white);font-family:Montserrat,sans-serif;font-weight:700;font-size:13px;display:flex;align-items:center;justify-content:center;letter-spacing:.3px}
h2.section-title{position:absolute;font-family:Montserrat,sans-serif;font-weight:700;font-size:34px;line-height:35px;color:var(--ink)}
.copy{position:absolute;font-size:13px;line-height:21px;color:#444}
.photo{position:absolute}
.featured{position:absolute;left:0;top:1230px;width:1200px;height:564px;background:var(--grey-bg)}
.card{position:absolute;top:156px;width:257px;height:327px;background:var(--white);border:1px solid #ddd}
.card .photo{left:0;top:0;width:255px;height:197px}
.tag{position:absolute;left:0;top:103px;background:var(--white);color:var(--orange);font-size:12px;padding:6px 14px}
.price{position:absolute;left:0;top:138px;background:var(--orange);color:var(--white);font-family:Roboto,sans-serif;font-weight:700;font-size:21px;padding:9px 14px}
.address{position:absolute;left:0;top:214px;width:100%;text-align:center;font-size:14px;line-height:22px;color:#555}
.specs{position:absolute;left:0;top:276px;width:100%;display:flex;justify-content:center;gap:24px;font-size:16px;color:#aaa}
.specs span{display:flex;align-items:center;gap:8px}
.show-off{position:absolute;left:0;top:2244px;width:1200px;height:553px;background:linear-gradient(120deg,#dfe6ee,#eef1f4 55%,#e6e9ec)}
.testimonial{position:absolute;left:0;top:2797px;width:1200px;height:378px;text-align:center}
.quote{position:absolute;left:385px;top:185px;width:430px;font-size:13px;line-height:21px;color:#555;text-align:center}
.author{position:absolute;left:0;top:289px;width:100%;font-size:21px;color:var(--orange);font-weight:500}
.dots{position:absolute;left:570px;top:338px;display:flex;gap:8px}
.dots i{width:5px;height:5px;border-radius:50%;background:#bbb;display:block}
.site-footer{position:absolute;left:0;top:3175px;width:1200px;height:432px;background:linear-gradient(180deg,#38383a,#2a2a2c)}
.site-footer .brand{left:0;top:55px;width:100%;text-align:center;font-size:40px;color:#d9d9d9;letter-spacing:3px}
.footer-nav{position:absolute;left:0;top:132px;width:100%;display:flex;justify-content:center;gap:32px;font-size:14px;color:#eee}
.footer-rule{position:absolute;left:150px;top:180px;width:900px;height:1px;background:#555}
.copyright{position:absolute;left:0;top:216px;width:100%;text-align:center;font-size:12px;color:#ddd}
.social{position:absolute;left:0;top:257px;width:100%;display:flex;justify-content:center;gap:22px}
.social i{width:24px;height:24px;border-radius:50%;background:#f1f1f1;display:block}
.badges{position:absolute;left:0;top:318px;width:100%;display:flex;justify-content:center;gap:12px}
.badges i{width:54px;height:54px;border-radius:50%;display:block;border:3px solid #e9e9e9}
</style>
</head>
<body>

<header class="site-header">
  <div class="abs brand">BRONWICK HOMES</div>
  <nav class="main-nav">
    <a class="active" style="left:362px">Home</a>
    <a style="left:425px">About</a>
    <a style="left:490px">Properties</a>
    <a style="left:578px">Why sell with us?</a>
    <a style="left:703px">Property Management</a>
    <a style="left:858px">More ⌄</a>
  </nav>
  <div class="phone">
    <svg width="15" height="15" viewBox="0 0 24 24"><path fill="#666" d="M6.6 10.8a15 15 0 0 0 6.6 6.6l2.2-2.2c.3-.3.7-.4 1-.2 1.1.4 2.3.6 3.6.6.6 0 1 .4 1 1V20c0 .6-.4 1-1 1A17 17 0 0 1 3 4c0-.6.4-1 1-1h3.5c.6 0 1 .4 1 1 0 1.3.2 2.5.6 3.6.1.3 0 .7-.2 1z"/></svg>
    Call us on: <span>0400 512 778</span>
  </div>
</header>

<section class="hero" role="img" aria-label="Bright living room with white sofa, patterned cushions and grey armchair">
  <h1 class="hero-title">THE BEST PROPERTY<br>BRONWICK OF YOUR LIFE!</h1>
</section>

<form class="search-box">
  <h2>SEARCH YOUR DREAM HOME TODAY</h2>
  <div class="field" style="left:29px;width:130px">City</div>
  <div class="field select" style="left:169px;width:177px">Property Type</div>
  <div class="field select" style="left:353px;width:172px">Sale Type</div>
  <div class="field" style="left:537px;width:110px">Min. Price</div>
  <div class="field" style="left:653px;width:116px">Max. Price</div>
  <div class="btn" style="left:788px;top:77px;width:105px;height:42px">SEARCH</div>
</form>

<section class="welcome">
  <h2 class="section-title" style="left:174px;top:838px">WELCOME TO<br>BRONWICK HOMES</h2>
  <p class="copy" style="left:174px;top:922px;width:416px">We're not your typical run-of-the-mill, traditional real estate agents. We focus on selling and managing residential real estate with a twist. Let's face it, the real estate industry has gone stale and has not kept up with the times and it still using the traditional methods of selling property which are antiquated. The market is craving for something new and fresh! So we're here to shake things up and save the day!</p>
  <div class="btn" style="left:174px;top:1063px;width:136px;height:48px">READ MORE</div>
  <div class="photo" style="left:613px;top:834px;width:453px;height:297px;background:linear-gradient(180deg,#2c4a6e 0%,#46556a 45%,#4f6a3a 80%,#5c8a3a 100%)" role="img" aria-label="Two-storey weatherboard family home at dusk with lit porch and lawn"></div>
</section>

<section class="featured">
  <h2 class="section-title" style="left:0;top:78px;width:1200px;text-align:center">OUR FEATURED LISTINGS</h2>

  <article class="card" style="left:172px">
    <div class="photo" style="background:linear-gradient(180deg,#f1f0ee,#d9d4ce)" role="img" aria-label="Bright apartment living room"></div>
    <div class="tag">For Rent</div><div class="price">$329,000</div>
    <p class="address">12/48 Alder Rd, Kelvin<br>Rise, Qld 4000</p>
    <div class="specs"><span>▬ 1</span><span>♨ 1</span><span>▭ 1</span></div>
  </article>

  <article class="card" style="left:471px">
    <div class="photo" style="background:linear-gradient(180deg,#4a86c8 0%,#9cc0de 40%,#c7c7c2 70%,#8a8a86 100%)" role="img" aria-label="Single-storey house with driveway under blue sky"></div>
    <div class="tag">For Rent</div><div class="price">$329,000</div>
    <p class="address">12/48 Alder Rd, Kelvin<br>Rise, Qld 4000</p>
    <div class="specs"><span>▬ 2</span><span>♨ 1</span><span>▭ 1</span></div>
  </article>

  <article class="card" style="left:769px">
    <div class="photo" style="background:linear-gradient(180deg,#9b7a5c 0%,#c9a98a 45%,#b5aba0 75%,#8d8680 100%)" role="img" aria-label="Elevated timber house with paved driveway"></div>
    <div class="tag">For Rent</div><div class="price">$329,000</div>
    <p class="address">12/48 Alder Rd, Kelvin<br>Rise, Qld 4000</p>
    <div class="specs"><span>▬ 4</span><span>♨ 2</span><span>▭ 2</span></div>
  </article>
</section>

<section class="difference">
  <h2 class="section-title" style="left:172px;top:1892px">THE BRONWICK<br>DIFFERENCE</h2>
  <p class="copy" style="left:172px;top:1974px;width:412px">At Bronwick, we don't even like calling ourselves 'agents' (which is why we go by 'Super Agents'). We understand the reputation, and we also understand that it NEEDS to change! Look, it's real estate, not rocket science. Selling property is easy enough that any monkey can just about do it (and there's probably a few out there); but there are those who do it with PANACHE, CREATIVITY, AND GENUINE CARE FOR THEIR CLIENTS</p>
  <div class="btn" style="left:172px;top:2138px;width:136px;height:48px">READ MORE</div>
  <div class="photo" style="left:626px;top:1880px;width:442px;height:288px;border-radius:18px;background:linear-gradient(135deg,#b9c6d3 0%,#e4e7ec 45%,#6a8a5a 100%)" role="img" aria-label="Video still of an agent by a waterfront"></div>
  <svg class="abs" style="left:818px;top:1997px" width="56" height="56" viewBox="0 0 56 56"><circle cx="28" cy="28" r="26" fill="rgba(0,0,0,.35)" stroke="#fff" stroke-width="2"/><path d="M22 17l17 11-17 11z" fill="#fff"/></svg>
</section>

<section class="show-off">
  <div class="photo" style="left:163px;top:82px;width:380px;height:376px;background:linear-gradient(135deg,#f7a24a,#f37a26 60%,#f8b56a)" role="img" aria-label="Interior photos of a bright apartment in orange tones"></div>
  <h2 class="section-title" style="left:601px;top:126px">WE KNOW HOW TO<br>SHOW OFF A PROPERTY!</h2>
  <p class="copy" style="left:601px;top:218px;width:425px">Most property videos are just straight-up boring!<br>WHY WOULD ANYONE BOTHER WATCHING WHAT'S ESSENTIALLY THE PROPERTY PICS IN MOTION? Our videos are different. With everyone searching for new properties online, we don't just want to capture their attention and stand out from the crowd, we want to leave a long-lasting impression. We also promote the lifestyle. Not just the property. New bars, the best restaurants, all of it!</p>
  <div class="btn" style="left:601px;top:2625px;width:136px;height:48px;top:381px">READ MORE</div>
</section>

<section class="testimonial">
  <h2 class="section-title" style="left:0;top:76px;width:1200px;text-align:center">HERE ARE SOME KIND WORDS<br>FROM SOME OF OUR RAVING FANS!</h2>
  <p class="quote">"Bronwick Homes have been great to my husband and I when it came to renting out our apartment. Dana helped make the process nice and easy for us and the communication has been outstanding. We would highly recommend Bronwick Homes."</p>
  <div class="author">Marlena Okafor</div>
  <div class="dots"><i></i><i></i><i></i><i></i><i></i></div>
</section>

<footer class="site-footer">
  <div class="abs brand">BRONWICK HOMES</div>
  <nav class="footer-nav"><span>Home</span><span>About</span><span>Properties</span><span>Why sell with us?</span><span>Property Management</span><span>More</span></nav>
  <div class="footer-rule"></div>
  <p class="copyright">Copyright 2020 Bronwickhomes. All Rights Reserved</p>
  <div class="social" aria-label="Social media links"><i></i><i></i><i></i><i></i><i></i></div>
  <div class="badges" aria-label="Industry awards">
    <i style="background:#6b5a3a"></i><i style="background:#2a8ad0"></i><i style="background:#3a9ac8"></i><i style="background:#f2f2f2"></i><i style="background:#3a9ac8"></i><i style="background:#f2f2f2"></i><i style="background:#e8e8e8"></i><i style="background:#f2f2f2"></i><i style="background:#e0a030"></i>
  </div>
</footer>

</body>
</html>
```